Business Card Design Project

We need a business card design for a new boutique consulting company, TivaConsulting. Our new logo has just been designed and we are looking for simple, clean looking business cards. Logo attached

Industry/Entity Type

Boutique

Requirements
Must have
• There must be room for each card to have the following details:
Name
Title
Address - 2 lines
Phone number
Email address
Website address

Nice to have
• May have something on the back of the buisness card - emphasing the word "Tiva".

```html
<!DOCTYPE html>
<html lang="en">
<head>
<meta charset="utf-8">
<title>TivaConsulting – Business Card</title>
<link href="https://fonts.googleapis.com/css2?family=Arimo:wght@400;700&display=swap" rel="stylesheet">
<style>
  :root {
    --green: #8fd400;
    --grey-text: #8b9093;
    --grey-bar: #a3a9ab;
    --bg-light: #ffffff;
    --bg-edge: #d9dcdd;
  }
  html, body {
    margin: 0;
    padding: 0;
    overflow: hidden;
    background: #ffffff;
  }
  .card {
    position: relative;
    width: 1200px;
    height: 685px;
    overflow: hidden;
    background: radial-gradient(ellipse 70% 75% at 52% 48%, var(--bg-light) 0%, #eef0f0 55%, var(--bg-edge) 100%);
    font-family: "Arimo", Arial, sans-serif;
  }
  .accent-top {
    position: absolute;
    top: 0;
    left: 524px;
    width: 676px;
    height: 39px;
    background: var(--green);
  }
  .accent-side {
    position: absolute;
    left: 0;
    top: 343px;
    width: 39px;
    height: 342px;
    background: var(--grey-bar);
  }
  .brand-name {
    position: absolute;
    left: 236px;
    top: 196px;
    margin: 0;
    font-family: "Arimo", Arial, sans-serif;
    font-size: 100px;
    font-weight: 400;
    line-height: 1;
    color: var(--grey-text);
  }
  .person {
    position: absolute;
    right: 539px;
    top: 446px;
    text-align: right;
  }
  .person-name {
    margin: 0;
    font-size: 33px;
    font-weight: 700;
    line-height: 1.1;
    color: var(--green);
  }
  .person-title {
    margin: 4px 0 0;
    font-size: 22px;
    font-weight: 700;
    color: var(--grey-text);
  }
  .contact {
    position: absolute;
    left: 716px;
    top: 450px;
    margin: 0;
    padding: 0;
    list-style: none;
    font-size: 23px;
    font-weight: 700;
    color: var(--grey-text);
  }
  .contact li {
    display: flex;
    align-items: center;
    height: 31px;
  }
  .contact .icon {
    width: 24px;
    height: 24px;
    margin-right: 8px;
    flex: none;
  }
  .contact .icon * {
    fill: none;
    stroke: var(--green);
    stroke-width: 2;
  }
  .contact .icon .solid {
    fill: var(--green);
    stroke: none;
  }
</style>
</head>
<body>
  <main class="card">
    <div class="accent-top"></div>
    <div class="accent-side"></div>

    <h1 class="brand-name">TivaConsulting</h1>

    <div class="person">
      <p class="person-name">CONSULTANT NAME</p>
      <p class="person-title">Tiva Consultant</p>
    </div>

    <ul class="contact">
      <li>PO Box 48120</li>
      <li>Harbourton 6150 New Zealand</li>
      <li>
        <svg class="icon" viewBox="0 0 24 24" aria-hidden="true">
          <path class="solid" d="M6 3 L9 3 L10.5 8 L8.3 9.6 C9.4 12.2 11.5 14.4 14.2 15.6 L15.8 13.4 L21 15 L21 18 C21 19.6 19.6 21 18 21 C10 20.5 3.5 14 3 6 C3 4.4 4.4 3 6 3 Z"/>
        </svg>
        + 64 21555019
      </li>
      <li>
        <svg class="icon" viewBox="0 0 24 24" aria-hidden="true">
          <rect x="2.5" y="5.5" width="19" height="13"/>
          <path d="M2.5 5.5 L12 13 L21.5 5.5"/>
        </svg>
        xxxxxxxxxxx@tivaconsulting.com
      </li>
      <li>
        <svg class="icon" viewBox="0 0 24 24" aria-hidden="true">
          <circle cx="12" cy="12" r="9.5"/>
          <ellipse cx="12" cy="12" rx="4.2" ry="9.5"/>
          <path d="M2.5 12 H21.5 M4 7 H20 M4 17 H20"/>
        </svg>
        www.tivaconsulting.com
      </li>
    </ul>
  </main>
</body>
</html>
```